Power point presentation optimization, in terms of content design

I have a completed business presentation, with all the texting, but I need some design improvement in terms of text formatting, lettering, text boxes, arrows, bullets, shapes and their formatting, relative location of text boxes and pictures in the slide, etc, etc, so that this specific presentation becomes more visually appealing.
Our company power point template is available.
I´m providing our company power point template (to be used as a reference) as well as the presentation that needs to be improved.

Target Market(s)

Potential partner in business.

Industry/Entity Type

Health

Requirements
Nice to have
• More ellegant collors (more according to the template) on the picture of slide 7. A more elegant dollar image (slide 16).

```html
<!DOCTYPE html>
<html lang="pt">
<head>
<meta charset="utf-8">
<title>Centro Vita Digital – Apresentação</title>
<link href="https://fonts.googleapis.com/css2?family=Lato:wght@300;400;700;900&display=swap" rel="stylesheet">
<style>
  :root {
    --page-bg: #dcdcdd;
    --navy: #0f5f86;
    --blue-deep: #126a93;
    --blue-mid: #0a6f9a;
    --blue-bright: #16a0c9;
    --band-blue: #1787b4;
    --charcoal: #3d3f43;
    --light: #eceef0;
    --white: #ffffff;
  }
  * { box-sizing: border-box; margin: 0; padding: 0; }
  html, body {
    width: 1008px; height: 1200px; overflow: hidden;
    background: var(--page-bg);
    font-family: "Lato", sans-serif;
  }
  .slide { position: absolute; left: 44.6px; width: 919px; overflow: hidden;
    box-shadow: 0 1px 3px rgba(0,0,0,.25); }

  /* Title slide */
  .slide--title { top: 63px; height: 517px;
    background: linear-gradient(135deg, #13729b 0%, var(--blue-deep) 55%, #0d5a80 100%); }
  .slide--title .facet { position: absolute; width: 340px; height: 340px; transform: rotate(45deg);
    background: rgba(255,255,255,.04); }
  .brand { position: absolute; left: 123px; top: 137px; display: flex; align-items: flex-start; gap: 22px; }
  .brand__square { width: 122px; height: 122px; background: var(--white); margin-top: 6px; }
  .brand__name { color: var(--white); font-weight: 900; font-size: 60px; line-height: 60px; letter-spacing: 1px; }
  .brand__person { color: var(--white); font-weight: 300; font-size: 31px; letter-spacing: 1px; margin-top: 8px; }
  .headline { position: absolute; left: 0; right: 0; top: 398px; text-align: center;
    color: var(--white); font-weight: 900; font-size: 38px; letter-spacing: -.5px; }
  .url-band { position: absolute; left: 0; right: 0; top: 443px; height: 44px; background: var(--white); }
  .url-band__rule { position: absolute; top: 19.5px; height: 5px; background: var(--band-blue); }
  .url-band__rule--left { left: 0; width: 255px; }
  .url-band__rule--right { right: 0; width: 247px; }
  .url-band__text { position: absolute; left: 0; right: 0; top: 4px; text-align: center;
    color: var(--navy); font-weight: 700; font-size: 28px; }

  /* Content slide */
  .slide--content { top: 616px; height: 518px;
    background: linear-gradient(125deg, #e4e6e9 0%, #f3f4f5 45%, #e6e8ea 100%); }
  .section-bar { position: absolute; left: 0; top: 45px; width: 100%; height: 55px; }
  .section-bar__title { position: absolute; left: 44px; top: 13px; color: var(--white); font-weight: 700; font-size: 25px; }
  .section-bar__subtitle { position: absolute; left: 500px; top: 13px; color: var(--white); font-weight: 400; font-size: 25px; }
  .diagram { position: absolute; left: 0; top: 0; }
  .info-box { position: absolute; top: 219px; width: 246px; height: 158px;
    display: flex; justify-content: center; padding-top: 30px;
    color: var(--white); font-weight: 700; font-size: 17px; line-height: 21px; text-align: center; }
  .info-box--need { left: 44px; background: var(--blue-bright); }
  .info-box--growth { left: 629px; background: var(--blue-mid); }
  .hub-label { position: absolute; left: 379px; top: 276px; width: 161px; text-align: center;
    color: var(--charcoal); font-weight: 700; font-size: 17px; line-height: 21px; }
  .footer-brand { position: absolute; left: 44px; top: 482px; display: flex; gap: 6px; align-items: flex-start; }
  .footer-brand__square { width: 16px; height: 16px; background: var(--band-blue); margin-top: 2px; }
  .footer-brand__name { color: var(--band-blue); font-weight: 900; font-size: 12px; line-height: 12px; }
  .footer-brand__person { color: #666; font-weight: 400; font-size: 6.5px; margin-top: 1px; }
  .footer-url { position: absolute; left: 554px; top: 490px; color: var(--white); font-weight: 700; font-size: 18px; }
</style>
</head>
<body>

<section class="slide slide--title">
  <div class="facet" style="left:640px; top:-120px;"></div>
  <div class="facet" style="left:-160px; top:140px;"></div>
  <div class="facet" style="left:700px; top:260px;"></div>
  <div class="brand">
    <div class="brand__square"></div>
    <div>
      <div class="brand__name">CENTRO VITA<br>DIGITAL</div>
      <div class="brand__person">Professora Doutora Helena Ramos</div>
    </div>
  </div>
  <h1 class="headline">UMA PERSPETIVA DE 5 MINUTOS</h1>
  <div class="url-band">
    <div class="url-band__rule url-band__rule--left"></div>
    <div class="url-band__rule url-band__rule--right"></div>
    <div class="url-band__text">www.centrovitadigital.com</div>
  </div>
</section>

<section class="slide slide--content">
  <svg class="section-bar" width="919" height="55" viewBox="0 0 919 55">
    <polygon points="0,0 481,0 452,55 0,55" fill="var(--charcoal)"/>
    <polygon points="481,0 919,0 919,55 452,55" fill="var(--blue-bright)"/>
  </svg>
  <h2 class="section-bar__title" style="top:58px;">IMAGIOLOGIA EM ANGOLA</h2>
  <div class="section-bar__subtitle" style="top:58px;">CONTEXTO DE OPORTUNIDADE</div>

  <svg class="diagram" width="919" height="518" viewBox="0 0 919 518">
    <line x1="290" y1="296.6" x2="365" y2="296.6" stroke="var(--blue-bright)" stroke-width="2.5"/>
    <line x1="555" y1="296.6" x2="629" y2="296.6" stroke="var(--blue-mid)" stroke-width="2.5"/>
    <circle cx="322" cy="296.6" r="5.5" fill="var(--white)" stroke="var(--blue-bright)" stroke-width="2"/>
    <circle cx="592" cy="296.6" r="5.5" fill="var(--white)" stroke="var(--blue-mid)" stroke-width="2"/>
    <polygon points="419,200 501,200 559,258 559,340 501,398 419,398 361,340 361,258"
             fill="var(--white)" stroke="var(--blue-mid)" stroke-width="10"/>
  </svg>

  <div class="info-box info-box--need">Carência dramática de<br>cuidados na área da<br>Imagiologia</div>
  <div class="info-box info-box--growth">População urbana em<br>rápido crescimento.<br>Aumento do PIB</div>
  <div class="hub-label">Oportunidade<br>comercial relevante</div>

  <svg class="diagram" width="919" height="518" viewBox="0 0 919 518">
    <polygon points="237,471 919,471 919,518 209,518" fill="var(--band-blue)"/>
    <line x1="275" y1="492" x2="537" y2="492" stroke="var(--white)" stroke-width="2"/>
  </svg>
  <div class="footer-brand">
    <div class="footer-brand__square"></div>
    <div>
      <div class="footer-brand__name">CENTRO VITA<br>DIGITAL</div>
      <div class="footer-brand__person">Professora Doutora Helena Ramos</div>
    </div>
  </div>
  <div class="footer-url">www.centrovitadigital.com&nbsp; I&nbsp; 01</div>
</section>

</body>
</html>
```